Brightwave Reach - Business Card

We need a business card for a Social Media Marketing company that specializes in online marketing for small businesses in Canada using common Social Media platforms such as Pictora, Kinloop, Blinkit & Chirpo.

I have uploaded a copy of our logo which I would like utilized in the business card. We would like the business card to be modern yet classy design.

Our website is www.brightwavereach.ca

Industry/Entity Type

Marketing

Contact Information for Business Card

Email: info@brightwavereach.ca
Website: www.brightwavereach.ca
Telephone: 604-392-5108

Colors

Designer to choose colors to be used in the design.

Requirements
Must have
• Social Media icons on reverse
• Please add some designs with color.

```html
<!DOCTYPE html>
<html lang="en">
<head>
<meta charset="utf-8">
<title>Brightwave Reach – Business Card</title>
<link rel="stylesheet" href="https://fonts.googleapis.com/css2?family=Questrial&display=swap">
<style>
  :root {
    --page: #2a2a2a;
    --card: #121212;
    --ink: #ffffff;
    --ink-soft: #e6e6e6;
    --faint: #4a4a4a;
    --band: #5a5a5a;
    --band-dark: #3c3c3c;
    --icon-bg: #6e6e6e;
  }
  * { box-sizing: border-box; margin: 0; padding: 0; }
  html, body { width: 1200px; height: 900px; overflow: hidden; }
  body {
    background: var(--page);
    font-family: "Questrial", "Century Gothic", sans-serif;
    color: var(--ink);
    position: relative;
  }
  .card {
    position: absolute;
    top: 100px;
    width: 400px;
    height: 700px;
    background: var(--card);
    overflow: hidden;
    box-shadow: 0 12px 30px rgba(0,0,0,.45);
  }
  .card--front { left: 160px; }
  .card--back { left: 640px; }

  /* Front */
  .brand {
    position: absolute;
    top: 200px;
    left: 0;
    width: 100%;
    display: flex;
    flex-direction: column;
    align-items: center;
    gap: 18px;
  }
  .brand__mark {
    width: 22px;
    height: 22px;
    background: var(--ink);
  }
  .brand__name {
    font-size: 44px;
    line-height: 1.05;
    text-align: center;
    text-transform: uppercase;
    letter-spacing: 2px;
    color: var(--ink);
  }
  .contact {
    position: absolute;
    left: 0;
    bottom: 70px;
    list-style: none;
    display: flex;
    flex-direction: column;
    gap: 10px;
  }
  .contact__row {
    display: flex;
    align-items: center;
    height: 34px;
  }
  .contact__bar {
    width: 70px;
    height: 22px;
    background: var(--ink);
    margin-right: 8px;
  }
  .contact__icon {
    width: 34px;
    height: 34px;
    background: var(--icon-bg);
    display: flex;
    align-items: center;
    justify-content: center;
    margin-right: 14px;
    flex: none;
  }
  .contact__text {
    font-size: 18px;
    letter-spacing: 0.5px;
    color: var(--ink-soft);
    white-space: nowrap;
  }

  /* Back */
  .brand--faint { top: 150px; }
  .brand--faint .brand__name { color: var(--faint); font-size: 46px; }
  .brand--faint .brand__mark { background: var(--faint); }
  .back-band {
    position: absolute;
    left: 0;
    bottom: 0;
    width: 400px;
    height: 260px;
  }
  .social {
    position: absolute;
    right: 28px;
    bottom: 250px;
    display: flex;
    gap: 14px;
    list-style: none;
  }
  .social__item {
    display: flex;
    align-items: center;
    gap: 6px;
    font-size: 16px;
    color: var(--ink);
  }
  .social__dot {
    width: 12px;
    height: 12px;
    background: var(--ink);
  }
</style>
</head>
<body>

<section class="card card--front" aria-label="Card front">
  <div class="brand">
    <span class="brand__mark"></span>
    <p class="brand__name">Brightwave<br>Reach</p>
  </div>

  <ul class="contact">
    <li class="contact__row">
      <span class="contact__bar"></span>
      <span class="contact__icon">
        <svg width="18" height="18" viewBox="0 0 24 24" aria-hidden="true"><path fill="#fff" d="M6.6 10.8a15.2 15.2 0 0 0 6.6 6.6l2.2-2.2c.3-.3.7-.4 1-.2 1.1.4 2.3.6 3.6.6.6 0 1 .4 1 1V20c0 .6-.4 1-1 1A17 17 0 0 1 3 4c0-.6.4-1 1-1h3.5c.6 0 1 .4 1 1 0 1.3.2 2.5.6 3.6.1.3 0 .7-.2 1z"/></svg>
      </span>
      <span class="contact__text">604-392-5108</span>
    </li>
    <li class="contact__row">
      <span class="contact__bar"></span>
      <span class="contact__icon">
        <svg width="20" height="16" viewBox="0 0 24 18" aria-hidden="true"><rect x="1" y="1" width="22" height="16" fill="none" stroke="#fff" stroke-width="2"/><path d="M1 1l11 9 11-9" fill="none" stroke="#fff" stroke-width="2"/></svg>
      </span>
      <span class="contact__text">info@brightwavereach.ca</span>
    </li>
    <li class="contact__row">
      <span class="contact__bar"></span>
      <span class="contact__icon">
        <svg width="20" height="20" viewBox="0 0 24 24" aria-hidden="true"><g fill="none" stroke="#fff" stroke-width="1.6"><circle cx="12" cy="12" r="10"/><ellipse cx="12" cy="12" rx="4.5" ry="10"/><path d="M2 12h20M4 6.5h16M4 17.5h16"/></g></svg>
      </span>
      <span class="contact__text">www.brightwavereach.ca</span>
    </li>
  </ul>
</section>

<section class="card card--back" aria-label="Card back">
  <div class="brand brand--faint">
    <span class="brand__mark"></span>
    <p class="brand__name">Brightwave<br>Reach</p>
  </div>

  <ul class="social">
    <li class="social__item"><span class="social__dot"></span>Pictora</li>
    <li class="social__item"><span class="social__dot"></span>Kinloop</li>
    <li class="social__item"><span class="social__dot"></span>Chirpo</li>
  </ul>

  <svg class="back-band" viewBox="0 0 400 260" aria-hidden="true">
    <polygon points="400,40 400,60 0,210 0,190" fill="#ffffff"/>
    <polygon points="400,75 400,145 0,250 0,235 150,160" fill="#5a5a5a"/>
    <polygon points="0,240 400,128 400,138 0,250" fill="#3c3c3c"/>
  </svg>
</section>

</body>
</html>
```